Gestaltung von Honigetiketten
Zielgruppe
Ich bin ein Imker, der im eigenen Restaurant seinen Honig ausstellen und verkaufen möchte.
Aufgabenstellung
Ich möchte exklusive und edle Honigetiketten die auffallen. Bevorzugt mit den Farben Gold und Schwarz, siehe meinem bisher gesehenen Favoriten im Anhang.
Nur das Logo selbst (Baum) soll übernommen werden Farbe kann variieren, ebenso die Schrift ist variabel.
Auf die Vorderseite des Honigetiketts soll zu lesen sein:
- Deutscher Honig
- Sommertracht
- 500g
- Logo und Name
Auf der Rückseite des Honigetiketts soll zu finden sein:
- freies Feld für Stempel für Namen und Adresse des Abfüllers
- freies Feld für das Mindesthaltbarkeitsdatum

```html
<!DOCTYPE html>
<html lang="de">
<head>
<meta charset="utf-8">
<title>Honigetikett – Gasthof am Ahorn Holmersaal</title>
<link href="https://fonts.googleapis.com/css2?family=Lato:wght@300;400;700;900&family=Open+Sans:wght@400;600&family=Kaushan+Script&display=swap" rel="stylesheet">
<style>
  :root{
    --paper:#ffffff;
    --label-dark:#0b0b0c;
    --label-mid:#2c2c2d;
    --gold-light:#f3dc8f;
    --gold:#c9a24a;
    --gold-deep:#8c6424;
    --leaf:#16923f;
    --text-grey:#a7a7a7;
    --field-red:#e2231a;
  }
  html,body{margin:0;padding:0;overflow:hidden;background:var(--paper);}
  .canvas{width:1199px;height:1200px;display:block;}
  .sans{font-family:"Lato",sans-serif;}
  .info-text{font-family:"Lato",sans-serif;font-weight:300;fill:var(--text-grey);}
  .vertical-claim{font-family:"Open Sans",sans-serif;fill:var(--text-grey);}
  .variety{font-family:"Kaushan Script",cursive;fill:var(--leaf);}
  .brand-name{font-family:"Lato",sans-serif;font-weight:900;fill:var(--gold);}
  .field-value{font-family:"Open Sans",sans-serif;fill:var(--field-red);}
  .stamp-note{font-family:"Open Sans",sans-serif;font-weight:600;fill:var(--field-red);}
</style>
</head>
<body>
<svg class="canvas" viewBox="0 0 1920 1920" preserveAspectRatio="none" xmlns="http://www.w3.org/2000/svg">
  <defs>
    <linearGradient id="band-fill" x1="0" x2="1" y1="0" y2="0">
      <stop offset="0" stop-color="var(--label-dark)"/>
      <stop offset="0.5" stop-color="var(--label-mid)"/>
      <stop offset="1" stop-color="var(--label-dark)"/>
    </linearGradient>
    <linearGradient id="gold-line" x1="0" x2="1" y1="0" y2="1">
      <stop offset="0" stop-color="var(--gold-light)"/>
      <stop offset="0.5" stop-color="var(--gold)"/>
      <stop offset="1" stop-color="var(--gold-deep)"/>
    </linearGradient>
  </defs>

  <!-- label body -->
  <g class="label-shape">
    <rect x="272" y="1178" width="1387" height="436" fill="url(#band-fill)"/>
    <polygon points="886,247 1045,247 1123,385 1045,522 1044,522 1044,1103 1135,1103 1177,1178 1177,1614 1135,1687 796,1687 755,1614 755,1178 796,1103 887,1103 887,522 886,522 807,385" fill="#262627"/>
  </g>

  <!-- gold frame -->
  <path class="gold-frame" d="M899,270 L1032,270 L1098,385 L1030,498 L1015,498 L1015,1137 L1115,1137 L1264,1395 L1115,1652 L815,1652 L666,1395 L815,1137 L917,1137 L917,498 L901,498 L833,385 Z" fill="none" stroke="url(#gold-line)" stroke-width="5"/>

  <!-- neck emblem -->
  <g class="neck-mark">
    <circle cx="962" cy="380" r="76" fill="none" stroke="url(#gold-line)" stroke-width="5"/>
    <circle cx="962" cy="380" r="66" fill="none" stroke="var(--leaf)" stroke-width="4"/>
    <text class="brand-name" x="962" y="388" font-size="22" text-anchor="middle">Am Ahorn</text>
  </g>

  <text class="vertical-claim" transform="translate(960,898) rotate(-90)" font-size="29" font-weight="600">QUALITÄTSHONIG</text>
  <text class="vertical-claim" transform="translate(988,922) rotate(-90)" font-size="23">aus kontrollier Produktion</text>

  <!-- front emblem -->
  <g class="front-mark">
    <circle cx="966" cy="1300" r="138" fill="none" stroke="url(#gold-line)" stroke-width="8"/>
    <circle cx="966" cy="1300" r="122" fill="none" stroke="var(--leaf)" stroke-width="6"/>
  </g>
  <rect x="722" y="1352" width="78" height="80" rx="30" fill="var(--gold)" role="img" aria-label="Goldene Biene"/>
  <rect x="1131" y="1338" width="58" height="94" rx="29" fill="var(--gold)" role="img" aria-label="Goldener Bienenkorb"/>

  <text class="brand-name" x="966" y="1504" font-size="42" text-anchor="middle">Gasthof am Ahorn</text>
  <text class="brand-name" x="966" y="1556" font-size="42" text-anchor="middle">Holmersaal</text>
  <text class="variety" x="966" y="1636" font-size="50" text-anchor="middle">Miel de Fleurs</text>

  <!-- back side: fields -->
  <text class="info-text" x="467" y="1236" font-size="22" text-anchor="middle" font-weight="400">Deutscher Honig</text>
  <text class="info-text" x="463" y="1294" font-size="19" text-anchor="middle">Los Nr.</text>
  <rect x="393" y="1299" width="141" height="31" fill="var(--paper)"/>
  <text class="field-value" x="463" y="1321" font-size="18" text-anchor="middle">AB54893C</text>
  <text class="info-text" x="463" y="1382" font-size="19" text-anchor="middle">Mindestens haltbar bis:</text>
  <rect x="393" y="1398" width="141" height="31" fill="var(--paper)"/>
  <text class="field-value" x="463" y="1420" font-size="18" text-anchor="middle">17/11/2020</text>
  <rect x="322" y="1478" width="282" height="104" fill="var(--paper)"/>
  <text class="stamp-note" x="463" y="1519" font-size="14" text-anchor="middle">freies Feld für Stempel für Namen un</text>
  <text class="stamp-note" x="461" y="1539" font-size="14" text-anchor="middle">Adresse des Abfüllers</text>

  <!-- back side: info -->
  <g class="info-text" font-size="19" text-anchor="middle">
    <text x="1436" y="1222">Gut verschlossen, kühl, trocken und</text>
    <text x="1436" y="1246">lichtgeschützt lagern. Kandierter Honig</text>
    <text x="1436" y="1271">wird durch  Erwärmen (Max. 40 Grad C)</text>
    <text x="1436" y="1295">wieder flüssig und streichfähig.</text>
  </g>
  <text class="info-text" x="1437" y="1362" font-size="42" font-weight="400" text-anchor="middle">500g Netto</text>

  <path class="icon-house" d="M1420,1416 L1436,1402 L1452,1416 L1447,1416 L1447,1428 L1425,1428 L1425,1416 Z" fill="var(--gold)"/>
  <g class="info-text" font-size="19" text-anchor="middle">
    <text x="1436" y="1456">Gasthaus Am Ahorn-Holmersaal</text>
    <text x="1436" y="1479">Birkenweg 12</text>
    <text x="1436" y="1503">90999 Talheim-Au</text>
  </g>
  <circle class="icon-phone" cx="1366" cy="1533" r="9" fill="none" stroke="var(--gold)" stroke-width="2"/>
  <text class="info-text" x="1386" y="1539" font-size="19">01234 / 56 00</text>
  <rect class="icon-fax" x="1357" y="1561" width="20" height="12" rx="2" fill="none" stroke="var(--gold)" stroke-width="2"/>
  <text class="info-text" x="1386" y="1573" font-size="19">01234 / 5 67 89</text>
</svg>
</body>
</html>
```